Geschäftspapiere für Rechtsanwaltskanzlei
Zielgruppe
Rechtsanwaltskanzlei
Aufgabenstellung
Bitte inklusive Logo (sollte Recht, Digital/Apps, Medizin illustrieren) - habe das Preisgeld vor diesem Hintergrund erhöht.
Die Kanzlei arbeitet an der Schnittstelle von (Medizin-)Recht und Digital. Von daher wären wären Symbole/Gestaltung aus Bereich Medizin, Recht und Digital (z.B. Apps etc.) passend.
Das Briefpapier soll alle wichtigen Infos enthalten, aber dabei sehr klar gehalten werden und nicht überladen sein. Mir ist ein schlichtes und ansprechendes Design wichtig. Es soll nicht verspielt sein.
Info auf Briefpapier:
Kanzlei für Medizinrecht
Rechtsanwalt Dr. Tilman Brecke - Fachanwalt für Medizinrecht
Bitte Platzhalter/Freitextfelder für die anderen anderen Angaben, wie:
- Adresse
- Telefon-Nr.
- Homepage
- E-Mail
- Bankdaten.

```html
<!DOCTYPE html>
<html lang="de">
<head>
<meta charset="utf-8">
<title>Briefpapier – Kanzlei Dr. Tilman Brecke</title>
<link href="https://fonts.googleapis.com/css2?family=Barlow:wght@400;500&display=swap" rel="stylesheet">
<style>
  :root {
    --backdrop: #ececec;
    --paper: #ffffff;
    --teal: #3596b5;
    --gold: #c8b27d;
    --ink: #5a5a5a;
    --ink-soft: #777777;
    --watermark: #f4f4f4;
  }
  * { margin: 0; padding: 0; box-sizing: border-box; }
  html, body {
    width: 1200px; height: 840px; overflow: hidden;
    background: var(--backdrop);
    font-family: "Barlow", Arial, sans-serif;
    color: var(--ink);
  }
  .letterhead {
    position: absolute; left: 317px; top: 20px;
    width: 566px; height: 800px;
    background: var(--paper);
    overflow: hidden;
    box-shadow: 0 2px 10px rgba(0,0,0,.12);
  }
  .bar { position: absolute; height: 9px; background: var(--teal); }
  .bar--top { left: 0; top: 0; width: 248px; }
  .bar--bottom { left: 310px; top: 765px; width: 256px; height: 8px; }

  .sender {
    position: absolute; left: 31px; top: 30px;
    font-style: normal; font-size: 8.6px; line-height: 12.4px; color: var(--ink);
  }
  .sender .contact { margin-top: 6px; }
  .label { color: var(--teal); }
  .sender .label { display: inline-block; min-width: 23px; }

  .brand-dot {
    position: absolute; left: 318px; top: 61px;
    width: 14px; height: 14px; border-radius: 50%; background: var(--gold);
  }
  .brand { position: absolute; left: 341px; top: 50px; width: 192px; }
  .brand-name {
    font-size: 22px; font-weight: 500; letter-spacing: .5px; line-height: 26px;
    color: var(--ink); white-space: nowrap;
  }
  .brand-firm {
    display: flex; align-items: center; gap: 4px; margin-top: 1px;
    font-size: 8.6px; font-weight: 500; letter-spacing: 1.2px; color: var(--teal);
  }
  .brand-firm::before, .brand-firm::after {
    content: ""; flex: 1; height: .6px; background: var(--ink-soft);
  }
  .brand-tagline {
    margin-top: 2px; font-size: 10.4px; letter-spacing: .9px; color: var(--ink); white-space: nowrap;
  }

  .return-line {
    position: absolute; left: 102px; top: 156px;
    font-size: 8px; letter-spacing: .3px; color: var(--ink);
    border-bottom: .6px solid var(--ink-soft); padding-bottom: 1px; white-space: nowrap;
  }
  .fold-mark { position: absolute; left: 10px; top: 544px; width: 12px; height: 1px; background: var(--ink-soft); }

  .watermark { position: absolute; left: 268px; top: 555px; width: 300px; height: 300px; }

  .footer { position: absolute; top: 754px; font-size: 8.2px; line-height: 11.3px; white-space: nowrap; }
  .footer--bank { left: 31px; }
  .footer--register { left: 180px; }
  .footer-divider { position: absolute; left: 167px; top: 752px; width: 1px; height: 33px; background: var(--ink); }
</style>
</head>
<body>
<main class="letterhead">
  <div class="bar bar--top"></div>

  <address class="sender">
    <div>Birkenhainer Straße, 15</div>
    <div>16352 Lindental</div>
    <div>Feldau</div>
    <div class="contact">
      <div><span class="label">Tel.</span> +49 000 000 74 3820</div>
      <div><span class="label">Fax.</span> +49 000 000 74 3821</div>
      <div><span class="label">Mail.</span> info@brecke-recht.de</div>
      <div><span class="label">Web.</span> www.brecke-recht.de</div>
    </div>
  </address>

  <span class="brand-dot"></span>
  <header class="brand">
    <div class="brand-name">Dr. Tilman Brecke</div>
    <div class="brand-firm">RECHTSANWÄLTE</div>
    <div class="brand-tagline">Fachanwalt für Medizinrecht</div>
  </header>

  <div class="return-line">Birkenhainer Straße, 15 • 16352 Lindental • Feldau</div>
  <div class="fold-mark"></div>

  <svg class="watermark" viewBox="0 0 300 300" aria-hidden="true">
    <circle cx="150" cy="150" r="145" fill="var(--watermark)"/>
  </svg>

  <div class="footer footer--bank">
    <div><span class="label">Bank:</span> Sparkasse Rheinaue</div>
    <div><span class="label">IBAN:</span> DE XX 52010XX 4800017395</div>
    <div><span class="label">BIC-Swift:</span> RHAUDEOOXXX</div>
  </div>
  <div class="footer-divider"></div>
  <div class="footer footer--register">
    <div>Amtsgericht Talheim</div>
    <div><span class="label">Handelsregister:</span> 0000731</div>
    <div><span class="label">USt.-ID-Nr.:</span> DE0007310000</div>
  </div>

  <div class="bar bar--bottom"></div>
</main>
</body>
</html>
```